Business Cards for an 'affordable luxury' inner city home builder in Calgary.

We need a business card design that emulates the progressive, innovative, culture of our company and the modern style of our homes. Use our website www.velmarbuilds-ex.com as a reference for the product we build.

Our company builds homes in the inner city space of Calgary, Alberta. We build affordable luxury.

Target Market(s)

Young professional Families

Contact Information for Business Card

Try to maintain consistency with the logo font and the card font.

Requirements
Must have
• The details must include: Name, education, title, phone number, website and email (Address is not as important)
• The design must be uniques (like our logo), elegant, sophisticated and modern.

```html
<!DOCTYPE html>
<html lang="en">
<head>
<meta charset="utf-8">
<title>Velmar Builds Ltd — Business Card</title>
<link href="https://fonts.googleapis.com/css2?family=Bebas+Neue&family=Work+Sans:wght@400;500&display=swap" rel="stylesheet">
<style>
  :root {
    --backdrop: #1c1c1e;
    --card-dark: #2a2a2b;
    --card-light: #ffffff;
    --ink: #1d1d1d;
    --ink-soft: #3a3a3a;
    --accent: #1ea7f2;
    --on-dark: #ffffff;
  }
  * { box-sizing: border-box; margin: 0; padding: 0; }
  html, body { width: 1200px; height: 900px; overflow: hidden; }
  body {
    background: var(--backdrop);
    display: flex;
    flex-direction: column;
    align-items: center;
    justify-content: center;
    gap: 40px;
    font-family: "Work Sans", Arial, sans-serif;
  }
  .card {
    width: 665px;
    height: 380px;
    position: relative;
    box-shadow: 0 12px 30px rgba(0,0,0,.45);
  }

  /* Front */
  .card--front {
    background: var(--card-light);
    border-right: 5px solid var(--accent);
    color: var(--ink);
  }
  .identity {
    position: absolute;
    left: 62px;
    top: 118px;
    width: 248px;
    text-align: right;
  }
  .identity__name {
    font-family: "Bebas Neue", Impact, sans-serif;
    font-size: 46px;
    letter-spacing: 1px;
    line-height: 1;
    text-align: left;
  }
  .identity__title {
    font-size: 17px;
    color: var(--ink-soft);
    margin-top: 4px;
  }
  .divider {
    position: absolute;
    left: 330px;
    top: 150px;
    width: 1.5px;
    height: 70px;
    background: var(--ink);
  }
  .contact-list {
    position: absolute;
    left: 350px;
    top: 150px;
    list-style: none;
    font-size: 17px;
    line-height: 24px;
  }
  .contact-list li { display: flex; align-items: center; gap: 9px; }
  .contact-list svg { width: 12px; height: 12px; flex: none; }
  .address {
    position: absolute;
    left: 62px;
    bottom: 58px;
    font-size: 16px;
    color: var(--ink-soft);
  }

  /* Back */
  .card--back {
    background: var(--card-dark);
    color: var(--on-dark);
    display: flex;
    align-items: center;
    justify-content: center;
    gap: 28px;
  }
  .brand-mark {
    width: 34px;
    height: 34px;
    background: var(--on-dark);
  }
  .brand-name {
    font-family: "Work Sans", Arial, sans-serif;
    font-weight: 500;
    font-size: 44px;
    line-height: 1.05;
    letter-spacing: 2px;
    text-transform: uppercase;
  }
</style>
</head>
<body>
  <section class="card card--front" aria-label="Business card front">
    <div class="identity">
      <h1 class="identity__name">Daniel Reeve</h1>
      <p class="identity__title">Director</p>
    </div>
    <div class="divider"></div>
    <ul class="contact-list">
      <li>
        <svg viewBox="0 0 12 12" aria-hidden="true"><path d="M2.5 1h2l1 2.8-1.3 1a6 6 0 0 0 3 3l1-1.3 2.8 1v2a1 1 0 0 1-1 1A9.5 9.5 0 0 1 1.5 2a1 1 0 0 1 1-1z" fill="#1d1d1d"/></svg>
        403-555-0147
      </li>
      <li>
        <svg viewBox="0 0 12 12" aria-hidden="true"><rect x="1" y="2.5" width="10" height="7" fill="none" stroke="#1d1d1d" stroke-width="1.2"/><path d="M1 2.5l5 4 5-4" fill="none" stroke="#1d1d1d" stroke-width="1.2"/></svg>
        projects@velmarbuilds-ex.com
      </li>
      <li>
        <svg viewBox="0 0 12 12" aria-hidden="true"><circle cx="6" cy="6" r="5" fill="none" stroke="#1d1d1d" stroke-width="1.1"/><ellipse cx="6" cy="6" rx="2.2" ry="5" fill="none" stroke="#1d1d1d" stroke-width="1"/><path d="M1 6h10" stroke="#1d1d1d" stroke-width="1"/></svg>
        www.velmarbuilds-ex.com
      </li>
    </ul>
    <p class="address">482 17 Ave NE Calgary, AB</p>
  </section>

  <section class="card card--back" aria-label="Business card back">
    <div class="brand-mark"></div>
    <p class="brand-name">Velmar<br>Builds<br>Ltd</p>
  </section>
</body>
</html>
```